Calloway Law - New Letterhead/Logo

Hello!
THE FIRM NAME IS NOW CALLOWAY LAW. We recently just changed our name and we are in need of a classy letterhead. Attached I have a logo we have included in the past, but we are willing to look at other alternatives as well. I will also attach our current letterhead with our old name, Calloway & Associates. We are willing to go without attorney names. Please help! Thanks
Updates
Project Deadline Extended Reason: Haven't found anything we love Added Tuesday, November 1, 2016

```html
<!DOCTYPE html>
<html lang="en">
<head>
<meta charset="utf-8">
<title>Calloway Law Letterhead</title>
<link rel="stylesheet" href="https://fonts.googleapis.com/css2?family=Cinzel:wght@400&display=swap">
<style>
  :root {
    --paper: #ffffff;
    --ink: #141414;
    --rule: #b39a7a;
    --accent: #b08a5c;
  }
  html, body {
    margin: 0;
    padding: 0;
    width: 1200px;
    height: 1200px;
    overflow: hidden;
    background: var(--paper);
  }
  .letterhead {
    position: relative;
    width: 1200px;
    height: 1200px;
    background: var(--paper);
    color: var(--ink);
    font-family: "Cinzel", "Times New Roman", serif;
  }
  .brand {
    position: absolute;
    left: 194px;
    top: 82px;
    display: flex;
    align-items: center;
    gap: 12px;
  }
  .brand-mark {
    width: 12px;
    height: 12px;
    border-radius: 50%;
    background: var(--accent);
  }
  .brand-name {
    font-size: 38px;
    line-height: 1;
    letter-spacing: 0.5px;
    color: var(--ink);
    white-space: nowrap;
  }
  .attorneys {
    position: absolute;
    right: 190px;
    top: 76px;
    margin: 0;
    padding: 0;
    list-style: none;
    text-align: right;
    font-size: 16.5px;
    line-height: 20px;
    letter-spacing: 0.6px;
  }
  .header-rule {
    position: absolute;
    left: 194px;
    top: 165px;
    width: 816px;
    height: 0;
    border-top: 1.5px solid var(--rule);
  }
  .contact {
    position: absolute;
    left: 0;
    top: 1110px;
    width: 1200px;
    text-align: center;
    font-size: 16.5px;
    line-height: 20px;
    letter-spacing: 0.6px;
  }
  .contact p { margin: 0; }
  .sep { margin: 0 9px; }
</style>
</head>
<body>
  <main class="letterhead">
    <header>
      <div class="brand">
        <span class="brand-mark" aria-hidden="true"></span>
        <span class="brand-name">Calloway Law</span>
      </div>
      <ul class="attorneys">
        <li>Marcus T Calloway, Esq.</li>
        <li>Ellis R. Whitford, Esq.</li>
        <li>Owen P, Varnell, Esq.</li>
      </ul>
      <div class="header-rule"></div>
    </header>
    <footer class="contact">
      <p>4120 Meridian Parkway<span class="sep">•</span>Suite 610<span class="sep">•</span>Aspen Ridge, Colorado 80199</p>
      <p>Phone: (555) 014-2870<span class="sep">•</span>Fax: (555) 014-2871<span class="sep">•</span>www.callowaylaw.net</p>
    </footer>
  </main>
</body>
</html>
```